Maple drift now Banner promoting freedom and adventure working from laptop

I need 3 different banners in 4 different sizes
I am an online business working from home on my laptop. I am in the motivational program and internet marketing industry and would like some banners that reflect healthy, fun and financially free lifestyle.
I have a Pallorum page title of KeyUpVibe and a website called Mapledriftnow.com
I have uploaded some photos but am unsure what may be required for the banners.
I am on the Gold Coast Australia but will be advertising in America, UK, Canada etc.

Target Market(s)

Adventure and Health fitness

Colors

Designer to choose colors to be used in the design.

Requirements
Must have
• Promotion of a living a financially free life through the ability of working from home via your own online business.
• Fun fit healthy freedom and adventure associated with someone living their dream life from working from home away from the 9 to 5 hustle and bussle.
Nice to have
• beaches, mountains and working from a Zen slate max.
• Showing fun and adventure from someone living this lifestyle.

```html
<!DOCTYPE html>
<html lang="en">
<head>
<meta charset="utf-8">
<title>Maple drift now – Work From Home Banner</title>
<link rel="stylesheet" href="https://fonts.googleapis.com/css2?family=Open+Sans:wght@300;700&display=swap">
<style>
  :root {
    --frame: #ffffff;
    --ink: #2e3233;
    --button: #2f3536;
    --button-text: #ffffff;
    --badge: rgba(255, 255, 255, 0.86);
    --wood-dark: #4e3321;
    --wood-light: #8a6142;
    --sky: #2f86d8;
    --sky-light: #9fd0f5;
    --sea: #39c3c9;
    --sand: #e9dcc2;
    --beach-sky: #6aa6dd;
    --beach-water: #7fa3b8;
    --grass: #b9aa7a;
    --office-light: #eceae6;
    --office-mid: #c9c4bd;
    --shirt: #3c4f7a;
  }
  * { margin: 0; padding: 0; box-sizing: border-box; }
  html, body {
    width: 1200px;
    height: 1200px;
    overflow: hidden;
    background: var(--frame);
    font-family: "Open Sans", Arial, sans-serif;
  }
  .banner {
    position: relative;
    width: 1200px;
    height: 1200px;
    background: var(--frame);
  }
  .photo {
    position: absolute;
    width: 570px;
    height: 570px;
  }
  .photo--desk-laptop {
    left: 20px; top: 20px;
    background: linear-gradient(135deg, var(--wood-light) 0%, var(--wood-dark) 55%, var(--wood-light) 100%);
  }
  .photo--tropical-beach {
    left: 610px; top: 20px;
    background: linear-gradient(180deg, var(--sky) 0%, var(--sky-light) 45%, var(--sea) 62%, var(--sea) 78%, var(--sand) 100%);
  }
  .photo--beach-selfie {
    left: 20px; top: 610px;
    background: linear-gradient(180deg, var(--beach-sky) 0%, #b6d3ee 35%, var(--beach-water) 48%, var(--sand) 70%, var(--grass) 100%);
  }
  .photo--office-desk {
    left: 610px; top: 610px;
    background: linear-gradient(160deg, var(--office-light) 0%, var(--office-mid) 60%, var(--shirt) 100%);
  }
  .badge {
    position: absolute;
    left: 251px;
    top: 243px;
    width: 714px;
    height: 714px;
    border-radius: 50%;
    background: var(--badge);
  }
  .copy {
    position: absolute;
    left: 228px;
    width: 760px;
    text-align: center;
    color: var(--ink);
  }
  .headline {
    top: 368px;
    font-weight: 700;
    font-size: 100px;
    line-height: 100px;
    letter-spacing: 1px;
  }
  .tagline {
    top: 574px;
    font-weight: 700;
    font-size: 38px;
    line-height: 46px;
  }
  .lifestyle {
    top: 626px;
    font-weight: 300;
    font-size: 38px;
    line-height: 49px;
  }
  .cta {
    position: absolute;
    left: 392px;
    top: 740px;
    width: 421px;
    height: 70px;
    background: var(--button);
    color: var(--button-text);
    font-weight: 300;
    font-size: 40px;
    line-height: 70px;
    text-align: center;
    text-decoration: none;
  }
  .website {
    top: 871px;
    font-weight: 700;
    font-size: 21px;
    line-height: 26px;
    letter-spacing: 0.5px;
  }
</style>
</head>
<body>
<main class="banner">
  <div class="photo photo--desk-laptop" role="img" aria-label="Laptop on a wooden desk seen from above, a hand holding a coffee cup"></div>
  <div class="photo photo--tropical-beach" role="img" aria-label="Tropical beach with palm fronds, turquoise water and an island under a blue sky"></div>
  <div class="photo photo--beach-selfie" role="img" aria-label="Smiling man taking a selfie on a beach with a red-sailed ship behind him"></div>
  <div class="photo photo--office-desk" role="img" aria-label="Person in a checked shirt working on a laptop at a desk with a coffee mug"></div>

  <div class="badge"></div>

  <h1 class="copy headline">WORK<br>FROM HOME</h1>
  <p class="copy tagline">WITH YOUR LAPTOP AND PHONE</p>
  <p class="copy lifestyle">CREATE THE LIFESTYLE<br>YOU ALWAYS WANTED</p>
  <a class="cta" href="#">CLICK HERE</a>
  <p class="copy website">WWW.MAPLEDRIFTNOW.COM</p>
</main>
</body>
</html>
```